Business Card Design

Just looking for a good designs that looks good with our company logo. I'd like it to be simple and to the point. Just including contact information, our logo, and my name somewhere on the card so future clients know who they're contacting, and a couple services offered. The two images I attached are pictures of our logo. I don't care which color they they are, I just attached both images to give a reference of logo colors depending on the color of the card.
Names: Calvin Prewitt
Phone: 555-247-9061
Email: tidyturfcrew@mailvista.net
Services offered:
Mowing
Fertilization
Aeration
Bed & tree maintenance
and more.
Industry/Entity Type
Business
Contact Information for Business Card
Names: Calvin Prewitt
Phone: 555-247-9061
Look and feel

```html
<!DOCTYPE html>
<html lang="en">
<head>
<meta charset="UTF-8">
<title>Tidy Turf Crew — Business Card</title>
<link rel="stylesheet" href="https://fonts.googleapis.com/css2?family=Arimo:wght@400&family=Jost:wght@500;600&display=swap">
<style>
  :root {
    --backdrop: #d9d9d9;
    --card: #2f3034;
    --accent: #e8503a;
    --ink: #ffffff;
  }
  * { box-sizing: border-box; margin: 0; padding: 0; }
  html, body {
    width: 1200px;
    height: 1199px;
    overflow: hidden;
    background: var(--backdrop);
  }
  .card {
    position: absolute;
    left: 50px;
    top: 278px;
    width: 1100px;
    height: 643px;
    background: var(--card);
    color: var(--ink);
  }
  .card__edge {
    position: absolute;
    left: 0;
    top: 0;
    width: 36px;
    height: 100%;
    background: var(--accent);
  }
  .services {
    position: absolute;
    left: 97px;
    top: 72px;
    list-style: none;
    font-family: "Arimo", Arial, sans-serif;
    font-size: 25px;
    line-height: 34px;
  }
  .brand {
    position: absolute;
    left: 869px;
    top: 191px;
    transform: translate(-50%, -50%);
    display: flex;
    align-items: center;
    gap: 16px;
    white-space: nowrap;
  }
  .brand__dot {
    width: 34px;
    height: 34px;
    border-radius: 50%;
    background: var(--accent);
  }
  .brand__name {
    font-family: "Jost", "Futura", sans-serif;
    font-weight: 600;
    font-size: 44px;
    color: var(--ink);
    letter-spacing: 0.5px;
  }
  .contact {
    position: absolute;
    right: 101px;
    top: 440px;
    text-align: right;
  }
  .contact__name {
    font-family: "Jost", "Futura", sans-serif;
    font-weight: 600;
    font-size: 34px;
    letter-spacing: 1px;
    margin-bottom: 28px;
  }
  .contact__line {
    font-family: "Arimo", Arial, sans-serif;
    font-size: 23px;
    line-height: 30px;
  }
</style>
</head>
<body>
  <article class="card">
    <div class="card__edge"></div>
    <ul class="services">
      <li>Mowing</li>
      <li>Fertilization</li>
      <li>Aeration</li>
      <li>Bed &amp; tree maintenance</li>
      <li>and more.</li>
    </ul>
    <div class="brand">
      <span class="brand__dot"></span>
      <span class="brand__name">Tidy Turf Crew</span>
    </div>
    <div class="contact">
      <p class="contact__name">Calvin Prewitt</p>
      <p class="contact__line">555-247-9061</p>
      <p class="contact__line">tidyturfcrew@mailvista.net</p>
    </div>
  </article>
</body>
</html>
```